Business Card Needed for Crafter of Pottery, Jewelry and Artwork

Calling all designers in search of an artistic challenge.

I need a new business card design for my pottery, jewelry and artwork business, Woven Glass and Tide, based in Vancouver BC.

I would like a card that is bright and inviting and preferably incorporates my logo and a sample of photos of my work while having a clean fresh look. The following contact details would preferably be included on the card as well:
• Helena Pikeworth
• Designer
• Phone: 604.555.0172
• Email: Designer@WovenGlassandTide.example
• Website: www.WovenGlassandTide.example
• Blog: www.ShapingHillside.example

The logo is attached in two color schemes in both Vector and Source formats. On past cards I’ve also included photos of my work. By including photos of the work the pieces are showcased and it catches people’s eye and prompts them to pick up the card and look at it more closely. For example, if I leave a stack in a coffee shop I want people to be drawn to the card, to pick it up and get a sense of the my product lines. Please feel free to pull photos of my work directly off of my website. If you need photos with higher pixels please let me know and I’ll email them directly to you. The website background is bffbda (191, 251, 218). I would like the business cards to match the feel of the website for consistency but the cards do not need to use the exact same colors. My website and current business card are predominantly turquoise shades. The background uses stripes provided by the website template. I don’t know the exact colors of the stripes.

My current business card is attached to show the use of photos in a design. Please note that I am not thrilled with my own design and am looking for variations and completely new designs. This example is not meant to be used as a template or starting point.

Here is some background surrounding my company:
WGT offers one of a kind jewelry, pottery, artwork and leather bags each designed with a twist. The pottery varies from rustic every day functional ware to raku artwork. The jewelry ranges from simple sterling every day pieces to multimedia pieces incorporating stone, metal, ceramics and fabric. The artwork is multimedia, typically acrylic paired with a natural element such as bark. All the bags are leather with reworked kimono fabric or patterned silk lining.

Feel free to check out my website to get a flavour for my work and the color scheme I've used on marketing materials so far. www.wovenglassandtide.example
Updates

Thank you to everyone who has submitted a design so far. I hope everyone has received some helpful feedback.

I'm going to post a survey to customers and friends asking for their votes. If you have new designs to submit please try to get them in by Saturday March 30 at noon so that I can include it in the survey launch.

Thank you

Target Market(s)

Females aged 25-65 interested in one of a kind functional pottery and jewelry.

Industry/Entity Type

Coffee Shop

Requirements
Must have
• Contact information, website, blog
Nice to have
• Logo, photos

```html
<!DOCTYPE html>
<html lang="en">
<head>
<meta charset="utf-8">
<title>Woven Glass and Tide — Business Card</title>
<link href="https://fonts.googleapis.com/css2?family=Archivo:ital,wght@0,600;0,800;1,900&family=Cinzel:wght@600&display=swap" rel="stylesheet">
<style>
  :root {
    --navy: #25215e;
    --teal: #13a898;
    --paper: #f6f6f4;
    --frame: #e6e6ea;
    --frame-edge: #c9c9d2;
    --backdrop: #dcdcdc;
  }
  * { box-sizing: border-box; margin: 0; padding: 0; }
  html, body { width: 1200px; height: 1000px; overflow: hidden; }
  body {
    background: var(--backdrop);
    font-family: "Archivo", Arial, sans-serif;
    position: relative;
  }
  .card {
    position: absolute;
    left: 250px;
    width: 700px;
    height: 400px;
    box-shadow: 0 6px 18px rgba(0,0,0,.18);
    overflow: hidden;
  }
  .card--front { top: 60px; background: var(--paper); }
  .card--back { top: 540px; background: var(--navy); }

  /* front */
  .front-shape { position: absolute; inset: 0; }
  .brand-seal {
    position: absolute;
    left: 45px; top: 45px;
    width: 230px; height: 230px;
    border-radius: 50%;
    background: #fff;
    border: 6px solid var(--navy);
    box-shadow: 0 0 0 10px #fff;
    display: flex; align-items: center; justify-content: center;
    text-align: center;
  }
  .brand-name {
    font-family: "Cinzel", Georgia, serif;
    font-weight: 600;
    font-size: 24px;
    line-height: 1.2;
    color: var(--navy);
    letter-spacing: 1px;
    padding: 0 28px;
  }
  .person {
    position: absolute;
    right: 40px; top: 70px;
    text-align: right;
    font-style: italic;
    font-weight: 900;
    line-height: 1;
  }
  .person-name { font-size: 38px; color: var(--navy); letter-spacing: -0.5px; }
  .person-name .surname { color: var(--teal); }
  .person-role { font-size: 22px; color: var(--navy); margin-top: 2px; letter-spacing: 1px; }

  .contact-list {
    position: absolute;
    left: 360px; top: 220px;
    width: 300px;
    list-style: none;
    display: flex; flex-direction: column; gap: 7px;
  }
  .contact-row { display: flex; gap: 6px; height: 26px; }
  .contact-icon {
    width: 34px; height: 26px;
    background: var(--navy);
    border-radius: 5px;
    display: flex; align-items: center; justify-content: center;
  }
  .contact-icon svg { width: 16px; height: 16px; }
  .contact-text {
    flex: 1;
    background: var(--navy);
    color: #fff;
    border-radius: 5px;
    font-size: 13px; font-weight: 600;
    display: flex; align-items: center; justify-content: center;
  }
  .contact-row--phone .contact-text { margin-left: 40px; letter-spacing: 1px; }

  /* back */
  .showcase-frame {
    position: absolute;
    background: var(--frame);
    border: 1px solid var(--frame-edge);
    clip-path: polygon(0 28px, 28% 28px, 28% 14px, 40% 14px, 40% 0, 60% 0, 60% 14px, 72% 14px, 72% 28px, 100% 28px, 100% 100%, 0 100%);
  }
  .showcase-frame--pottery { left: 30px; top: 30px; width: 160px; height: 345px; }
  .showcase-frame--jewelry { left: 268px; top: 40px; width: 130px; height: 335px; }
  .showcase-frame--bags { left: 440px; top: 85px; width: 230px; height: 290px; }
  .showcase-photo {
    position: absolute;
    left: 12px; right: 12px; top: 40px; bottom: 20px;
  }
  .showcase-frame--pottery .showcase-photo { background: linear-gradient(180deg, #d9c4ad, #3a3434 40%, #e4d4c4 60%, #3a3434); }
  .showcase-frame--jewelry .showcase-photo { background: linear-gradient(180deg, #c8c4bc, #4aa98a 35%, #d6a84a 60%, #6ec3a4 80%, #cfcac2); }
  .showcase-frame--bags .showcase-photo { background: linear-gradient(180deg, #e8e3d8, #1faaa0 30%, #8c8a86 55%, #1faaa0 80%, #eae6de); }
</style>
</head>
<body>

<section class="card card--front" aria-label="Business card front">
  <svg class="front-shape" viewBox="0 0 700 400" width="700" height="400" aria-hidden="true">
    <path d="M0 0 H250 C350 80 350 300 140 400 H0 Z" fill="var(--teal)"/>
    <path d="M250 0 C350 80 350 300 140 400" fill="none" stroke="var(--navy)" stroke-width="4"/>
  </svg>

  <div class="brand-seal">
    <span class="brand-name">Woven Glass and Tide</span>
  </div>

  <div class="person">
    <p class="person-name">Helena <span class="surname">Pikeworth</span></p>
    <p class="person-role">DESIGNER</p>
  </div>

  <ul class="contact-list">
    <li class="contact-row">
      <span class="contact-icon"><svg viewBox="0 0 16 16" aria-hidden="true"><rect x="1.5" y="3.5" width="13" height="9" fill="none" stroke="#fff" stroke-width="1.4"/><path d="M1.5 3.5 L8 9 L14.5 3.5" fill="none" stroke="#fff" stroke-width="1.4"/></svg></span>
      <span class="contact-text">Designer@WovenGlassandTide.example</span>
    </li>
    <li class="contact-row">
      <span class="contact-icon"><svg viewBox="0 0 16 16" aria-hidden="true"><circle cx="8" cy="8" r="6.3" fill="none" stroke="#fff" stroke-width="1.4"/><path d="M1.7 8 H14.3 M8 1.7 C4.5 5 4.5 11 8 14.3 M8 1.7 C11.5 5 11.5 11 8 14.3" fill="none" stroke="#fff" stroke-width="1.2"/></svg></span>
      <span class="contact-text">www.WovenGlassandTide.example</span>
    </li>
    <li class="contact-row">
      <span class="contact-icon"><svg viewBox="0 0 16 16" aria-hidden="true"><rect x="2" y="2" width="12" height="12" rx="1.5" fill="none" stroke="#fff" stroke-width="1.4"/><path d="M4.5 5.5 H11.5 M4.5 8 H11.5 M4.5 10.5 H9" stroke="#fff" stroke-width="1.2"/></svg></span>
      <span class="contact-text">www.ShapingHillside.example</span>
    </li>
    <li class="contact-row contact-row--phone">
      <span class="contact-icon"><svg viewBox="0 0 16 16" aria-hidden="true"><path d="M4 1.5 L6.5 4.5 L5 6.5 C6 8.5 7.5 10 9.5 11 L11.5 9.5 L14.5 12 L12.5 14.5 C7 14 2 9 1.5 3.5 Z" fill="#fff"/></svg></span>
      <span class="contact-text">604.555.0172</span>
    </li>
  </ul>
</section>

<section class="card card--back" aria-label="Business card back">
  <div class="showcase-frame showcase-frame--pottery">
    <div class="showcase-photo" role="img" aria-label="Photos of three pottery bowls with black zigzag rims"></div>
  </div>
  <div class="showcase-frame showcase-frame--jewelry">
    <div class="showcase-photo" role="img" aria-label="Photo of a green stone and amber bead necklace"></div>
  </div>
  <div class="showcase-frame showcase-frame--bags">
    <div class="showcase-photo" role="img" aria-label="Photos of a turquoise and grey leather clutch bag"></div>
  </div>
</section>

</body>
</html>
```